Government Contracting business needs a website design.

Brisco & Penwick, LLC is a minority owned Service Disabled Veteran Owned Small Business (SDVOSB) that provides Strategic Planning, Public Health Emergency Response, and Data Management Solutions for Federal Civilian and Defense Agencies. We have over 20 years of experience helping health and defense agencies develop concept of operations, deploy assets and personnel in Hot Zones around the world, and deliver goods and services all of the globe.

We are a leader in the field of Data Management. We help our customers develop cloud migration and disaster recovery strategies. We are experts with database management, data replication, queries, consolidation, and records management.

We are looking for a very nice and simple website designs that states clearly what we do as a company and that is easy for our customers to follow. We would like to have some moving pictures that are base on our expertise. We want the website to be easy to use and have the scroll down features that keeps things all on the same page when clicking on the menu. I attached a document with what we need on the website. I will also attach our logo. We want it to look simple clean and very professional.

Target Market(s)

Government Contracting, Management Consulting, Health

Industry/Entity Type

Government

Coding

Number of Pages Required

1 page

Font styles to use
Serif

Requirements
Must have
• Very nice picture slides that speaks to our capabilities in Disaster Response, Strategic Planning, and Database Management. Slick look and design. Make sure SDVOSB Logo is right at the beginning of website as our customers is looking for that certification. Very nice colors that blend well with our logo.
Nice to have
• Very nice and slick colors that blends well with logo.
Should not have
• Basic website design that are weary on the eye. No bright colors, just simple colors that looks good with logo.

```html
<!DOCTYPE html>
<html lang="en">
<head>
<meta charset="utf-8">
<title>Brisco &amp; Penwick, LLC</title>
<link href="https://fonts.googleapis.com/css2?family=Roboto:wght@300;400;500;700&family=Merriweather:wght@400;700&display=swap" rel="stylesheet">
<style>
:root{
  --navy:#1d2740;
  --navy-dark:#151c2f;
  --blue:#1f6cc0;
  --blue-deep:#164e8f;
  --orange:#f39c12;
  --ink:#333a45;
  --muted:#6b7280;
  --light:#eeeff1;
  --white:#ffffff;
}
*{box-sizing:border-box;margin:0;padding:0}
html,body{width:1200px;height:3756px;overflow:hidden}
body{font-family:"Roboto",Arial,sans-serif;color:var(--ink);background:var(--white);position:relative}
.abs{position:absolute}
h2.section-title{font-weight:500;font-size:34px;text-align:center;letter-spacing:.5px;color:var(--ink)}
.btn{display:inline-block;background:var(--orange);color:var(--white);font-size:13px;font-weight:500;padding:11px 30px;letter-spacing:.5px}
.btn-blue{background:var(--blue);color:var(--white);font-size:12px;font-weight:500;padding:8px 18px;display:inline-block}

/* header */
.site-header{top:0;left:0;width:1200px;height:180px;background:var(--navy)}
.brand{top:26px;left:60px;display:flex;align-items:center;gap:12px;color:var(--white)}
.brand .mark{width:34px;height:34px;background:var(--white)}
.brand span{font-family:"Merriweather",Georgia,serif;font-size:26px;font-weight:700}
.cert-badge{top:18px;left:1080px;width:64px;height:64px;border-radius:50%;background:var(--white);border:5px solid #c8102e}
.main-nav{top:130px;left:60px;display:flex;gap:34px;color:var(--white);font-size:14px;font-weight:500;letter-spacing:.5px}
.phone{top:124px;right:60px;color:var(--white);font-size:24px;font-weight:500;display:flex;align-items:center;gap:10px}

/* hero */
.hero{top:180px;left:0;width:1200px;height:520px;background:linear-gradient(160deg,#7b8a96 0%,#5f6b72 40%,#c8a23a 62%,#4a565d 100%)}
.hero-caption{top:360px;left:40px;width:470px;background:rgba(0,0,0,.55);padding:22px 26px;color:var(--white)}
.hero-caption h1{font-size:40px;font-weight:700;letter-spacing:1px}
.hero-caption p{font-size:22px;line-height:1.3;margin:8px 0 18px}

/* overview */
.overview{top:700px;left:0;width:1200px;height:348px;text-align:center}
.overview h2{margin-top:44px}
.overview .lead{width:1040px;margin:26px auto 0;font-size:14px;line-height:1.75;color:var(--muted)}
.overview .naics{margin-top:30px;font-size:20px;font-weight:500}
.overview .btn{margin-top:28px}

/* certifications */
.certs{top:1048px;left:0;width:1200px;height:112px;background:var(--light);display:flex;align-items:center;padding:0 60px;gap:36px}
.certs h3{font-size:22px;font-weight:500;margin-right:6px}
.certs .chip{height:34px;background:#c4c8ce;border-radius:4px}

/* services */
.services{top:1160px;left:0;width:1200px;height:410px;background:linear-gradient(180deg,#2a6fb5 0%,#1c5a9e 60%,#2d79c2 100%)}
.services h2{color:var(--white);margin-top:36px}
.svc-row{top:165px;left:62px;display:flex;gap:32px}
.svc-card{width:244px;height:226px;background:var(--white);padding:18px 18px 0;position:relative}
.svc-card svg{display:block;margin-bottom:8px}
.svc-card h4{font-size:13px;font-weight:700;color:var(--ink);text-transform:uppercase;line-height:1.3;margin-bottom:8px}
.svc-card ul{list-style:none;font-size:11px;line-height:1.75;color:var(--muted)}
.svc-card ul li:before{content:"\25AA";color:var(--blue);margin-right:6px}
.svc-card .btn{position:absolute;bottom:-16px;left:72px;font-size:11px;padding:8px 22px}

/* founder */
.founder{top:1570px;left:0;width:1200px;height:300px;text-align:center}
.founder h2{margin-top:24px}
.founder .name-bar{width:360px;margin:18px auto 0;background:var(--blue);color:var(--white);padding:10px 0}
.founder .name-bar strong{font-size:20px;font-weight:700;display:block}
.founder .name-bar span{font-size:13px}
.founder p{width:760px;margin:22px auto 0;font-size:14px;line-height:1.7;color:var(--muted)}
.founder .btn{margin-top:20px}

/* agencies */
.agencies{top:1870px;left:0;width:1200px;height:290px}
.agencies h2{margin-top:30px}
.agency-row{top:120px;left:0;width:1200px;display:flex;justify-content:center;gap:70px;align-items:center}

/* why */
.why{top:2160px;left:0;width:1200px;height:320px;background:var(--white)}
.why h2{position:absolute;top:30px;left:60px;font-size:30px;font-weight:500}
.why ul{position:absolute;top:90px;left:60px;width:520px;list-style:none;font-size:14px;line-height:1.55;color:var(--muted)}
.why li{padding-left:26px;position:relative;margin-bottom:14px}
.why li:before{content:"";position:absolute;left:0;top:5px;width:11px;height:11px;background:var(--orange)}
.why-photo{position:absolute;top:0;left:620px;width:580px;height:320px;background:linear-gradient(135deg,#3b4a5c 0%,#2a3b57 40%,#7a8694 100%)}

/* partners */
.partners{top:2480px;left:0;width:1200px;height:300px;background:var(--light)}
.partners h2{margin-top:30px}
.partner-row{top:110px;left:70px;display:flex;gap:40px}
.partner-card{width:235px;height:100px;background:var(--white);display:flex;align-items:center;justify-content:center}
.partner-card i{display:block;width:150px;height:30px;background:#b9bec6}

/* white papers */
.papers{top:2780px;left:0;width:1200px;height:540px;background:linear-gradient(180deg,#d9e6f2 0%,#3f86c7 30%,#1d5d9f 100%)}
.papers h2{color:var(--white);margin-top:54px;font-weight:400;letter-spacing:2px}
.paper{background:var(--white);width:300px;height:236px;padding:26px;text-align:center}
.paper h5{font-size:15px;font-weight:500;line-height:1.45;color:var(--ink);margin-bottom:20px}

/* footer */
.site-footer{top:3320px;left:0;width:1200px;height:436px;background:var(--navy);color:#c9cfda}
.footer-col{position:absolute;top:40px;font-size:13px;line-height:2.1}
.footer-col h6{font-size:14px;font-weight:500;color:var(--white);margin-bottom:12px;text-transform:uppercase;letter-spacing:.5px}
.footer-bottom{position:absolute;bottom:0;left:0;width:1200px;height:46px;background:var(--navy-dark)}
.social{display:flex;gap:12px;margin-top:16px}
.social i{display:block;width:22px;height:22px;border-radius:50%;background:#c9cfda}
</style>
</head>
<body>

<header class="site-header abs">
  <div class="brand abs"><div class="mark"></div><span>Brisco &amp; Penwick</span></div>
  <div class="cert-badge abs" role="img" aria-label="SDVOSB certification badge"></div>
  <nav class="main-nav abs"><span>HOME</span><span>ABOUT US</span><span>SERVICES</span><span>WHY HIRE US?</span><span>BLOG</span><span>PARTNERS</span><span>CONTACT US</span></nav>
  <div class="phone abs">
    <svg width="20" height="20" viewBox="0 0 24 24"><path fill="#fff" d="M6.6 10.8a15 15 0 0 0 6.6 6.6l2.2-2.2c.3-.3.7-.4 1-.2 1.1.4 2.3.6 3.6.6.6 0 1 .4 1 1V20c0 .6-.4 1-1 1A17 17 0 0 1 3 4c0-.6.4-1 1-1h3.5c.6 0 1 .4 1 1 0 1.3.2 2.5.6 3.6.1.3 0 .7-.2 1z"/></svg>
    202-555-0147
  </div>
</header>

<section class="hero abs" role="img" aria-label="Slide photo: heavy equipment clearing debris after a hurricane">
  <div class="hero-caption abs">
    <h1>HURRICANE</h1>
    <p>Lanventore veritatis et quasi architecto beatae vitae dicta sunt explicabo...</p>
    <span class="btn">READ MORE</span>
  </div>
</section>

<section class="overview abs">
  <h2 class="section-title">COMPANY OVERVIEW</h2>
  <p class="lead">Brisco &amp; Penwick, LLC is a minority owned Service Disabled Veteran Owned Small Business (SDVOSB) that provides Strategic Planning, Public Health Emergency Response, and Data Management Solutions for Federal Civilian and Defense Agencies. We have over 20 years of experience helping health and defense agencies develop concept of operations, deploy assets and personnel in Hot Zones around the world, and deliver goods and services all of the globe.</p>
  <p class="naics">Our company's NAICS codes - 541611, 541511, 541330, 541512, 641110</p>
  <span class="btn">READ MORE</span>
</section>

<section class="certs abs">
  <h3>Our IT certifications</h3>
  <i class="chip" style="width:90px"></i><i class="chip" style="width:110px"></i><i class="chip" style="width:40px;height:44px"></i><i class="chip" style="width:90px"></i><i class="chip" style="width:90px"></i><i class="chip" style="width:70px;height:40px"></i>
</section>

<section class="services abs">
  <h2 class="section-title">OUR SERVICES</h2>
  <div class="svc-row abs">
    <div class="svc-card">
      <svg width="40" height="34" viewBox="0 0 40 34" fill="none" stroke="#1f6cc0" stroke-width="2"><circle cx="20" cy="8" r="5"/><circle cx="7" cy="24" r="4"/><circle cx="33" cy="24" r="4"/><path d="M20 13v6M20 19L9 21M20 19l11 2"/></svg>
      <h4>Strategic Planning</h4>
      <ul><li>Organizational Needs Assessment</li><li>Business Development</li><li>Marketing Outreach</li><li>Cost Benefit and Allocation</li></ul>
      <span class="btn">READ MORE</span>
    </div>
    <div class="svc-card">
      <svg width="40" height="34" viewBox="0 0 40 34" fill="none" stroke="#c8102e" stroke-width="2"><path d="M20 31S4 21 4 11a8 8 0 0 1 16-2 8 8 0 0 1 16 2c0 10-16 20-16 20z"/><path d="M11 16h6l2-4 3 8 2-4h5"/></svg>
      <h4>Public Health Emergency Response</h4>
      <ul><li>Crisis Management</li><li>Disaster Relief Planning</li><li>Asset and Personnel Deployment</li><li>Personal Hazard Response</li></ul>
      <span class="btn">READ MORE</span>
    </div>
    <div class="svc-card">
      <svg width="40" height="34" viewBox="0 0 40 34" fill="none" stroke="#1f6cc0" stroke-width="2"><rect x="6" y="4" width="28" height="8"/><rect x="6" y="13" width="28" height="8"/><rect x="6" y="22" width="28" height="8"/></svg>
      <h4>Data Management Services</h4>
      <ul><li>Cloud Migration Strategy</li><li>Disaster Recovery Strategy</li><li>Records Management</li><li>Data Analytics</li></ul>
      <span class="btn">READ MORE</span>
    </div>
    <div class="svc-card">
      <svg width="40" height="34" viewBox="0 0 40 34" fill="none" stroke="#1f6cc0" stroke-width="2"><path d="M9 3h16l7 7v21H9z"/><path d="M14 14h13M14 19h13M14 24h9"/></svg>
      <h4>Contracts Vehicles</h4>
      <ul><li>SDVOSB Set-Aside</li><li>GSA Schedule 70 IT Services</li><li>GSA MAS Professional</li><li>CIO-SP3 Small</li><li>SEWP V</li></ul>
      <span class="btn">READ MORE</span>
    </div>
  </div>
</section>

<section class="founder abs">
  <h2 class="section-title">FOUNDER'S BIO</h2>
  <div class="name-bar"><strong>RET. SFC DARNELL R. OKAFOR</strong><span>Chief Executive Officer</span></div>
  <p>Brisco &amp; Penwick, LLC was founded by Retired Sergeant First Class (Ret. SFC) Darnell R. Okafor. He retired from the US Army after over 20 years of service which included tours in "Operation Desert Storm/Shield", two tours of duty at the DMZ in Korea, also served in various locations in Germany including the Berlin Wall, and a Tour in Bosnia-Herzegovina for operation "Deliberate Force".</p>
  <span class="btn">READ MORE</span>
</section>

<section class="agencies abs">
  <h2 class="section-title">AGENCIES WE SERVE</h2>
  <div class="agency-row abs">
    <i style="display:block;width:120px;height:80px;background:#c4c8ce"></i>
    <i style="display:block;width:180px;height:60px;background:#c4c8ce"></i>
    <i style="display:block;width:110px;height:90px;background:#c4c8ce"></i>
    <i style="display:block;width:140px;height:50px;background:#c4c8ce"></i>
  </div>
</section>

<section class="why abs">
  <h2>WHY HIRE US?</h2>
  <ul>
    <li>Over 20 years of experience deploying assets and personnel to disaster zones around the US and the world.</li>
    <li>Over 20 years of experience developing concept of operations and stakeholder management strategies for Federal Agencies.</li>
    <li>Over 15 years of experience with database management and replications.</li>
    <li>Highly educated consultants with over 90% possessing advance degrees and industry certifications.</li>
  </ul>
  <div class="why-photo" role="img" aria-label="Photo: paramedics attending to a patient during an emergency response"></div>
</section>

<section class="partners abs">
  <h2 class="section-title">OUR PARTNERS</h2>
  <div class="partner-row abs">
    <div class="partner-card"><i></i></div>
    <div class="partner-card"><i></i></div>
    <div class="partner-card"><i></i></div>
    <div class="partner-card"><i></i></div>
  </div>
</section>

<section class="papers abs">
  <h2 class="section-title">WHITE PAPER PUBLICATIONS</h2>
  <div class="paper abs" style="top:150px;left:120px">
    <h5>Drones for Aid: A Study on effective use of Unmanned Aerial Systems for Disaster Relief Planning</h5>
    <span class="btn-blue">DOWNLOAD NOW</span>
  </div>
  <div class="paper abs" style="top:120px;left:450px">
    <h5>Drones Infra Red Camera Technology: A study on how to use drones to facilitate crop dusting</h5>
    <span class="btn-blue">DOWNLOAD NOW</span>
  </div>
  <div class="paper abs" style="top:150px;left:780px">
    <h5>Cloud Computing - An acquisition strategy guide Cloud Migration Approach Best Practices Database Replication Pros and Cons</h5>
    <span class="btn-blue">DOWNLOAD NOW</span>
  </div>
</section>

<footer class="site-footer abs">
  <div class="footer-col" style="left:60px">
    <div style="display:flex;align-items:center;gap:10px;color:#fff"><i style="display:block;width:28px;height:28px;background:#fff"></i><span style="font-family:'Merriweather',Georgia,serif;font-size:22px;font-weight:700">Brisco &amp; Penwick</span></div>
    <p style="margin-top:28px;line-height:1.6">Copyright © 2018 Company Name.<br>All Rights Reserved</p>
    <div class="social"><i></i><i></i><i></i><i></i></div>
  </div>
  <div class="footer-col" style="left:420px">
    <h6>Site Map</h6>
    <div style="display:flex;gap:60px"><div>Home<br>About Us<br>Services<br>Why Hire Us?</div><div>Blog<br>Partners<br>Contact Us</div></div>
  </div>
  <div class="footer-col" style="left:650px">
    <h6>Our Capabilities</h6>
    Strategic Planning<br>Public Health Emergency Response<br>Data Management Services<br>Contracts Vehicles
  </div>
  <div class="footer-col" style="left:940px">
    <h6>Contact Info</h6>
    1200 Harbor Point Dr<br>Alexandria, VA 22314<br>202-555-0147<br>info@briscopenwick.com
  </div>
  <div class="footer-bottom"></div>
</footer>

</body>
</html>
```